Castastrophe General Contractor needs leave behind for sales

Will respond quickly to designer inquires
Fast winning selection
Will notify all of winning selection

Catastrophe Restoration General Contractor offering specialized services to the insurance industry. Sales meeting leave behind flyer for presentation to insurance agents. We would like for agents to refer policyholders to our company for complete residential and commercial restoration projects.

Some copy uploaded for reference. 5.5" x 8.5" approx - double sided color w/ sales business card reproduced on back side. Approved / Preferred Contractor for Brightshield, Vantacover, KRPQ & Fenlo insurance companies.

Larkmoor Company is a general contractor specialized in the restoration industry for both residential and commercial properties.
We have incorporated the best technology tools and partnered with a network of industry professionals across the country to provide the most efficient and comprehensive service available.
Website under construction: www.thelarkmoorcompany.example

Target Market(s)

Insurance Sale Agents

Industry/Entity Type

Residential

Requirements
Must have
• Brightshield, Vantacover & KRPQ & Halvey Dresmit logos. Space to reproduce business card on back.. Looking for concept deign where we can work w/ local designer if necessary to finalize. Open to different sized flyer dependent on design.

```html
<!DOCTYPE html>
<html lang="en">
<head>
<meta charset="utf-8">
<title>Larkmoor Company – Agent Leave-Behind</title>
<link href="https://fonts.googleapis.com/css2?family=Roboto+Condensed:wght@700&family=PT+Sans:wght@400;700&display=swap" rel="stylesheet">
<style>
:root{
  --blue:#2a7aa3;
  --navy:#1d5a86;
  --gold:#f6b21f;
  --ink:#2f2f2f;
  --grey:#6b6b6b;
  --paper:#ffffff;
  --stage:#ebe8e3;
  --photo-sky:#7fa9c9;
  --photo-house:#8a7a62;
}
*{box-sizing:border-box;margin:0;padding:0}
html,body{width:957px;height:1200px;overflow:hidden}
body{background:var(--stage);font-family:"PT Sans",sans-serif;color:var(--ink);position:relative}
.card{position:absolute;left:102px;width:753px;height:489px;background:var(--paper);overflow:hidden;box-shadow:0 3px 12px rgba(0,0,0,.25)}
.card--front{top:93px}
.card--back{top:612px}
.art{position:absolute;left:0;top:0}
.headline{position:absolute;left:34px;top:20px;color:#fff;font-family:"Roboto Condensed",sans-serif;font-weight:700;text-transform:uppercase;line-height:1.15}
.headline__kicker{font-size:19px}
.headline__main{font-size:23px;margin-top:10px}
.panel{position:absolute;background:var(--gold);border-radius:10px;padding:10px 14px 8px;box-shadow:0 2px 4px rgba(0,0,0,.15)}
.panel__title{color:#fff;font-weight:700;font-size:14px;text-transform:uppercase;margin-bottom:7px}
.panel__lead{font-weight:700;font-size:12px;margin-bottom:6px}
.checklist{list-style:none}
.checklist li{display:flex;gap:7px;font-size:10.5px;line-height:1.3;margin-bottom:6px}
.checklist svg{flex:none;margin-top:2px}
.panel--services{left:480px;top:24px;width:246px;height:141px}
.panel--benefits{left:480px;top:183px;width:246px;height:144px}
.contact-line{position:absolute;left:-22px;top:430px;font-weight:700;font-size:18px;color:var(--blue)}
.contact-line .label{color:var(--gold)}
.contact-email{position:absolute;left:-22px;top:456px;font-weight:700;font-size:18px;color:var(--blue)}
.front-contact{position:absolute;left:22px;top:0;width:400px;height:489px}
.brand{position:absolute;display:flex;flex-direction:column;align-items:center;gap:8px;color:var(--navy);font-weight:400}
.brand__dot{width:22px;height:22px;border-radius:50%;background:var(--gold)}
.brand--front{left:483px;top:355px;width:240px;font-size:27px}
.brand--back{left:30px;top:322px;width:170px;font-size:18px}
.section-tag{position:absolute;left:0;background:var(--navy);color:#fff;font-weight:700;font-size:14px;padding:4px 14px;border-radius:0 14px 14px 0;width:238px}
.section-tag--efficiency{top:20px}
.section-tag--quality{top:158px}
.back-list{position:absolute;left:22px;width:225px}
.back-list--efficiency{top:52px}
.back-list--quality{top:190px}
.back-list li{font-size:10px;color:var(--grey);margin-bottom:8px}
.call-box{position:absolute;left:225px;top:285px;width:220px;height:120px;background:var(--gold);border-radius:12px;text-align:center;padding-top:10px}
.call-box__label{color:#fff;font-weight:700;font-size:14px}
.call-box__phone{background:#fff;font-weight:700;font-size:26px;margin:6px 0 6px;padding:2px 0}
.call-box__web{font-weight:700;font-size:11px;line-height:1.4}
.partners{position:absolute;left:16px;right:16px;top:425px;height:50px;display:flex;align-items:center;justify-content:space-between}
.partner{display:flex;align-items:center;gap:5px;font-weight:700;font-size:13px;color:var(--navy);white-space:nowrap}
.partner__mark{width:16px;height:16px;background:var(--navy)}
.badge-rect{width:26px;height:46px;background:var(--navy);border-radius:3px}
.badge-square{width:28px;height:28px;background:#e9a1c6}
.badge-circle{width:36px;height:36px;border-radius:50%;background:var(--navy)}
.badge-circle--light{background:#6aa5d6}
</style>
</head>
<body>

<!-- FRONT -->
<section class="card card--front">
  <svg class="art" width="753" height="489" viewBox="0 0 753 489">
    <defs>
      <linearGradient id="frontPhoto" x1="0" y1="0" x2="0" y2="1">
        <stop offset="0" stop-color="var(--blue)"/>
        <stop offset=".35" stop-color="#6f98b8"/>
        <stop offset="1" stop-color="var(--photo-house)"/>
      </linearGradient>
    </defs>
    <path d="M0 0 H452 C488 130 440 268 310 318 C210 352 92 346 0 322 Z" fill="url(#frontPhoto)" role="img" aria-label="Photo of a two-storey house with shingle siding and a brown roof"/>
    <path d="M452 0 C488 130 440 268 310 318 C210 352 92 346 0 322" fill="none" stroke="var(--blue)" stroke-width="16"/>
    <path d="M470 0 C510 140 458 284 316 336 C212 370 90 362 0 340" fill="none" stroke="var(--gold)" stroke-width="8"/>
  </svg>

  <div class="headline">
    <div class="headline__kicker">Preferred Contractor Agent Support</div>
    <div class="headline__main">Providing claims support during<br>and after a cat event</div>
  </div>

  <div class="panel panel--services">
    <div class="panel__title">Agent Support Services</div>
    <ul class="checklist">
      <li><svg width="10" height="10" viewBox="0 0 10 10"><rect x=".5" y=".5" width="9" height="9" fill="#fff" stroke="#555"/><polyline points="2,5 4,7.5 8.5,2" fill="none" stroke="#333" stroke-width="1.4"/></svg>Guaranteed next day inspections from time of notification</li>
      <li><svg width="10" height="10" viewBox="0 0 10 10"><rect x=".5" y=".5" width="9" height="9" fill="#fff" stroke="#555"/><polyline points="2,5 4,7.5 8.5,2" fill="none" stroke="#333" stroke-width="1.4"/></svg>Damage status reporting directly back to Agent</li>
      <li><svg width="10" height="10" viewBox="0 0 10 10"><rect x=".5" y=".5" width="9" height="9" fill="#fff" stroke="#555"/><polyline points="2,5 4,7.5 8.5,2" fill="none" stroke="#333" stroke-width="1.4"/></svg>Assist policy holder in filing claim to CAT desk</li>
    </ul>
  </div>

  <div class="panel panel--benefits">
    <div class="panel__title">Agent Benefits:</div>
    <div class="panel__lead">Greater Satisfaction, Increased Retention</div>
    <ul class="checklist">
      <li><svg width="10" height="10" viewBox="0 0 10 10"><rect x=".5" y=".5" width="9" height="9" fill="#fff" stroke="#555"/><polyline points="2,5 4,7.5 8.5,2" fill="none" stroke="#333" stroke-width="1.4"/></svg>Increase policyholder satisfaction</li>
      <li><svg width="10" height="10" viewBox="0 0 10 10"><rect x=".5" y=".5" width="9" height="9" fill="#fff" stroke="#555"/><polyline points="2,5 4,7.5 8.5,2" fill="none" stroke="#333" stroke-width="1.4"/></svg>Demonstrate a greater commitment to customer satisfaction</li>
      <li><svg width="10" height="10" viewBox="0 0 10 10"><rect x=".5" y=".5" width="9" height="9" fill="#fff" stroke="#555"/><polyline points="2,5 4,7.5 8.5,2" fill="none" stroke="#333" stroke-width="1.4"/></svg>Follow up on outcome beyond the closing of a claim</li>
    </ul>
  </div>

  <div class="front-contact">
    <div class="contact-line"><span class="label">Contact us:</span> (800) 555-0142</div>
    <div class="contact-email">info@larkmoorcompany.example</div>
  </div>

  <div class="brand brand--front"><span class="brand__dot"></span>Larkmoor Company</div>
</section>

<!-- BACK -->
<section class="card card--back">
  <svg class="art" width="753" height="489" viewBox="0 0 753 489">
    <defs>
      <linearGradient id="backPhoto" x1="0" y1="0" x2="0" y2="1">
        <stop offset="0" stop-color="var(--photo-sky)"/>
        <stop offset=".45" stop-color="#6d7173"/>
        <stop offset="1" stop-color="var(--photo-house)"/>
      </linearGradient>
    </defs>
    <path d="M300 0 H753 V385 C620 400 430 380 335 300 C262 232 252 92 300 0 Z" fill="url(#backPhoto)" role="img" aria-label="Photo of a stone-faced house with a grey roof and gabled entry"/>
    <path d="M300 0 C252 92 262 232 335 300 C430 380 620 400 753 385" fill="none" stroke="var(--blue)" stroke-width="14"/>
    <path d="M282 0 C234 100 244 244 322 314 C420 398 620 418 753 404" fill="none" stroke="var(--gold)" stroke-width="7"/>
  </svg>

  <div class="section-tag section-tag--efficiency">Enhanced Efficiency</div>
  <ul class="checklist back-list back-list--efficiency">
    <li><svg width="10" height="10" viewBox="0 0 10 10"><rect x=".5" y=".5" width="9" height="9" fill="#fff" stroke="var(--navy)"/><polyline points="2,5 4,7.5 8.5,2" fill="none" stroke="var(--navy)" stroke-width="1.4"/></svg>Increase efficiency in moving from claim to restoration completion</li>
    <li><svg width="10" height="10" viewBox="0 0 10 10"><rect x=".5" y=".5" width="9" height="9" fill="#fff" stroke="var(--navy)"/><polyline points="2,5 4,7.5 8.5,2" fill="none" stroke="var(--navy)" stroke-width="1.4"/></svg>"In-house" systems closely linked to the insurer or administrator</li>
    <li><svg width="10" height="10" viewBox="0 0 10 10"><rect x=".5" y=".5" width="9" height="9" fill="#fff" stroke="var(--navy)"/><polyline points="2,5 4,7.5 8.5,2" fill="none" stroke="var(--navy)" stroke-width="1.4"/></svg>Shorten the timeline from claims settlement to finished repairs</li>
  </ul>

  <div class="section-tag section-tag--quality">Increased Quality Control</div>
  <ul class="checklist back-list back-list--quality">
    <li><svg width="10" height="10" viewBox="0 0 10 10"><rect x=".5" y=".5" width="9" height="9" fill="#fff" stroke="var(--navy)"/><polyline points="2,5 4,7.5 8.5,2" fill="none" stroke="var(--navy)" stroke-width="1.4"/></svg>Pre-screened and credentialed for license, insurance, and financial stability</li>
    <li><svg width="10" height="10" viewBox="0 0 10 10"><rect x=".5" y=".5" width="9" height="9" fill="#fff" stroke="var(--navy)"/><polyline points="2,5 4,7.5 8.5,2" fill="none" stroke="var(--navy)" stroke-width="1.4"/></svg>Monitored performance and control standards for higher-quality outcomes</li>
    <li><svg width="10" height="10" viewBox="0 0 10 10"><rect x=".5" y=".5" width="9" height="9" fill="#fff" stroke="var(--navy)"/><polyline points="2,5 4,7.5 8.5,2" fill="none" stroke="var(--navy)" stroke-width="1.4"/></svg>Background verification on all staff and field representatives</li>
  </ul>

  <div class="brand brand--back"><span class="brand__dot"></span>Larkmoor Company</div>

  <div class="call-box">
    <div class="call-box__label">Contact us:</div>
    <div class="call-box__phone">(800) 555-0142</div>
    <div class="call-box__web">info@larkmoorcompany.example<br>www.thelarkmoorcompany.example</div>
  </div>

  <div class="partners">
    <span class="badge-rect"></span>
    <span class="partner">Fenlo</span>
    <span class="partner"><span class="partner__mark" style="background:#c8352b"></span>Halvey Dresmit</span>
    <span class="badge-square"></span>
    <span class="partner"><span class="partner__mark"></span>Brightshield</span>
    <span class="partner">KRPQ</span>
    <span class="badge-circle"></span>
    <span class="partner">Vantacover</span>
    <span class="badge-circle badge-circle--light"></span>
    <span class="badge-circle badge-circle--light"></span>
  </div>
</section>

</body>
</html>
```